Need simple and modern looking business card with all my information on one side and logo on the other side
Info :
Company name - VELTRIN CONSTRUCTION LLC
Company addres- 418 maple 307th. Dunford hill ny 10583
Email- veltrinllc@pormail.Com
Company phone number 555-318-4096
Cell number- 555-762-0384
Web site - veltrinllc.Com
My name Gerald haverstrom

Target Market(s)

Construction , home improvement, remodeling

Industry/Entity Type

Construction

Contact Information for Business Card

It has to be moder but at the same time simple

Font styles to use
Sans Serif

Colors
0255a3
ffffff
000000
f78f20
b1b1b1
9d9d9d
1b1b1b
33a6d7
ec1f27

Requirements
Must have
• My logo on one side maybe with a some kind of background on the other side all my information
Nice to have
• Some kind of background pictures provided by you .PLEASE HAVE ACCOUNT WITH PIXVALEMOR WILL NOT PAY ANY EXTRA FEES .
Should not have
• Any kind of hamer, nails,screws, helmets itp. Please do not copy the other designs come up with something new.

```html
<!DOCTYPE html>
<html lang="en">
<head>
<meta charset="utf-8">
<title>Veltrin Construction LLC – Business Card</title>
<link rel="stylesheet" href="https://fonts.googleapis.com/css2?family=Lato:wght@400;700;900&family=Exo+2:wght@500&display=swap">
<style>
  :root {
    --stage: #2b2b2b;
    --card: #050505;
    --white: #ffffff;
    --orange: #f78f20;
    --blue: #33a6d7;
    --navy: #0255a3;
    --grey: #9d9d9d;
    --divider: #3a3a3a;
  }
  * { box-sizing: border-box; margin: 0; padding: 0; }
  html, body { width: 1200px; height: 900px; overflow: hidden; }
  body {
    background: var(--stage);
    display: flex;
    flex-direction: column;
    align-items: center;
    justify-content: center;
    gap: 36px;
    font-family: "Lato", sans-serif;
  }
  .card {
    width: 700px;
    height: 400px;
    background: var(--card);
    border-radius: 22px;
    position: relative;
    overflow: hidden;
  }
  .brand-name {
    color: var(--white);
    font-family: "Lato", sans-serif;
    font-weight: 900;
    text-transform: uppercase;
    line-height: 1;
  }
  .card-front {
    display: flex;
    align-items: center;
    justify-content: center;
  }
  .card-front .brand-name { font-size: 58px; letter-spacing: 2px; text-align: center; }
  .card-front .brand-name small { display: block; font-size: 26px; letter-spacing: 6px; margin-top: 10px; }

  .card-back {
    display: flex;
    align-items: center;
    padding: 0 50px;
  }
  .card-back .brand {
    width: 300px;
  }
  .card-back .brand-name { font-size: 46px; letter-spacing: 1px; }
  .card-back .brand-name small { display: block; font-size: 20px; letter-spacing: 3px; margin-top: 8px; }
  .divider {
    width: 1px;
    height: 190px;
    background: var(--divider);
    margin: 0 34px 0 10px;
  }
  .contact { color: var(--white); }
  .person {
    font-family: "Exo 2", sans-serif;
    font-weight: 500;
    font-size: 22px;
    letter-spacing: 1.5px;
    text-transform: uppercase;
    margin-bottom: 10px;
  }
  .person .first { color: var(--orange); }
  .person .last { color: var(--blue); }
  .address { font-size: 16px; line-height: 1.3; margin: 0 0 10px 18px; }
  .contact-list { list-style: none; }
  .contact-list li {
    display: flex;
    align-items: center;
    gap: 10px;
    font-size: 16px;
    line-height: 1.35;
  }
  .contact-list svg { width: 13px; height: 13px; flex: none; }
</style>
</head>
<body>

  <section class="card card-front">
    <p class="brand-name">Veltrin<small>Construction LLC</small></p>
  </section>

  <section class="card card-back">
    <div class="brand">
      <p class="brand-name">Veltrin<small>Construction LLC</small></p>
    </div>
    <div class="divider"></div>
    <div class="contact">
      <p class="person"><span class="first">Gerald</span> <span class="last">Haverstrom</span></p>
      <p class="address">418 maple 307th.<br>Dunford hill ny 10583</p>
      <ul class="contact-list">
        <li>
          <svg viewBox="0 0 16 16" aria-hidden="true"><path d="M4 1 L6.5 4.5 L5 6.5 Q6.5 9.5 9.5 11 L11.5 9.5 L15 12 L13 15 Q5 14 1 3 Z" fill="var(--blue)"/></svg>
          555-318-4096
        </li>
        <li>
          <svg viewBox="0 0 16 16" aria-hidden="true"><rect x="4" y="1" width="8" height="14" rx="1.5" fill="none" stroke="var(--blue)" stroke-width="1.6"/><circle cx="8" cy="12.3" r="0.9" fill="var(--blue)"/></svg>
          555-762-0384
        </li>
        <li>
          <svg viewBox="0 0 16 16" aria-hidden="true"><rect x="1" y="3" width="14" height="10" fill="none" stroke="var(--blue)" stroke-width="1.5"/><path d="M1 3 L8 9 L15 3" fill="none" stroke="var(--blue)" stroke-width="1.5"/></svg>
          veltrinllc@pormail.com
        </li>
        <li>
          <svg viewBox="0 0 16 16" aria-hidden="true"><circle cx="8" cy="8" r="6.5" fill="none" stroke="var(--blue)" stroke-width="1.4"/><ellipse cx="8" cy="8" rx="2.8" ry="6.5" fill="none" stroke="var(--blue)" stroke-width="1.2"/><path d="M1.5 8 H14.5" stroke="var(--blue)" stroke-width="1.2"/></svg>
          www.veltrinllc.com
        </li>
      </ul>
    </div>
  </section>

</body>
</html>
```